Fernvale Business Card Design

We are looking for a fresh business card design for our new logo. We would like a business card that is unique but friendly. We are in the window coverings business offering blinds, shutters and shades for homes.

Target Market(s)

Targeting the end-consumer

Industry/Entity Type

Business

Requirements
Must have
• Must have a dedicates space for a photo of our sales person. Must contain our new logo (attached).

```html
<!DOCTYPE html>
<html lang="en">
<head>
<meta charset="utf-8">
<title>Fernvale Business Card</title>
<link href="https://fonts.googleapis.com/css2?family=Questrial&display=swap" rel="stylesheet">
<style>
  :root {
    --backdrop: #ececec;
    --card-grey: #67686c;
    --band-black: #151515;
    --photo-black: #161616;
    --accent-green: #8dc63f;
    --text-white: #ffffff;
    --brand-grey: #77787c;
    --icon-grey: #606165;
    --footer-ink: #1f1f1f;
  }
  * { margin: 0; padding: 0; box-sizing: border-box; }
  html, body {
    width: 1200px; height: 1000px; overflow: hidden;
    background: var(--backdrop);
    font-family: "Questrial", "Century Gothic", sans-serif;
  }
  .canvas { position: relative; width: 1200px; height: 1000px; }

  .card {
    position: absolute; left: 205px; width: 790px; height: 450px;
    background: var(--card-grey); overflow: hidden;
  }
  .card--front { top: 35px; }
  .card--back { top: 510px; }

  /* Front */
  .photo-slot {
    position: absolute; left: 0; top: 115px; width: 218px; height: 218px;
    background: linear-gradient(180deg, #1c1c1c, var(--photo-black));
  }
  .person-name {
    position: absolute; left: 240px; top: 104px;
    font-size: 58px; line-height: 1; color: var(--text-white); letter-spacing: 0.5px;
  }
  .person-role {
    position: absolute; left: 241px; top: 167px;
    font-size: 28px; line-height: 1; color: var(--accent-green); letter-spacing: 0.5px;
  }
  .contact-rule {
    position: absolute; left: 240px; top: 210px; width: 445px; height: 2px;
    background: var(--accent-green);
  }
  .icon-bar {
    position: absolute; left: 240px; top: 210px; width: 32px; height: 123px;
    background: var(--accent-green);
  }
  .icon-bar svg { position: absolute; left: 6px; width: 20px; height: 20px; }
  .contact-list { position: absolute; left: 285px; top: 234px; list-style: none; }
  .contact-list li {
    font-size: 20px; line-height: 35.5px; color: var(--text-white); white-space: nowrap;
  }
  .footer-band {
    position: absolute; left: 0; bottom: 0; width: 100%; height: 55px;
    background: var(--band-black);
  }
  .brand-small {
    position: absolute; right: 32px; top: 14px;
    display: flex; align-items: center; gap: 10px;
    font-size: 24px; line-height: 1; color: var(--brand-grey);
  }
  .brand-small .brand-square { width: 26px; height: 26px; background: var(--brand-grey); }

  /* Back */
  .brand-band {
    position: absolute; left: 0; top: 138px; width: 100%; height: 172px;
    background: var(--band-black);
  }
  .brand-large {
    position: absolute; left: 92px; top: 20px; height: 132px;
    display: flex; align-items: center; gap: 50px;
    font-size: 84px; line-height: 1; color: var(--brand-grey);
  }
  .brand-large .brand-square { width: 106px; height: 132px; background: var(--brand-grey); }
  .back-web {
    position: absolute; left: 0; top: 412px; width: 100%; text-align: center;
    font-size: 18px; line-height: 1; color: var(--footer-ink);
  }
</style>
</head>
<body>
<main class="canvas">
  <section class="card card--front" aria-label="Business card front">
    <div class="photo-slot" role="img" aria-label="Portrait photo of the sales associate"></div>
    <h1 class="person-name">DANA REYES</h1>
    <p class="person-role">SALES ASSOCIATE</p>
    <div class="contact-rule"></div>
    <div class="icon-bar">
      <svg style="top:22px" viewBox="0 0 20 20" aria-hidden="true">
        <path d="M5 2 L8 2 L9 6 L7 8 Q9 12 12 13 L14 11 L18 12 L18 15 Q17 18 14 18 Q4 16 2 6 Q2 3 5 2 Z" fill="var(--icon-grey)"/>
      </svg>
      <svg style="top:58px" viewBox="0 0 20 20" aria-hidden="true" fill="none" stroke="var(--icon-grey)" stroke-width="1.4">
        <circle cx="10" cy="10" r="8.3"/>
        <ellipse cx="10" cy="10" rx="3.6" ry="8.3"/>
        <line x1="1.7" y1="10" x2="18.3" y2="10"/>
        <line x1="3" y1="5.5" x2="17" y2="5.5"/>
        <line x1="3" y1="14.5" x2="17" y2="14.5"/>
      </svg>
      <svg style="top:93px" viewBox="0 0 20 20" aria-hidden="true" fill="none" stroke="var(--icon-grey)" stroke-width="1.4">
        <rect x="1" y="4" width="18" height="12"/>
        <polyline points="1,4 10,11 19,4"/>
      </svg>
    </div>
    <ul class="contact-list">
      <li>+555.201.4830</li>
      <li>www.fernvaleshutters.com</li>
      <li>dana.reyes@fernvaleshutters.com</li>
    </ul>
    <div class="footer-band">
      <div class="brand-small"><span class="brand-square"></span><span>Fernvale</span></div>
    </div>
  </section>

  <section class="card card--back" aria-label="Business card back">
    <div class="brand-band">
      <div class="brand-large"><span class="brand-square"></span><span>Fernvale</span></div>
    </div>
    <p class="back-web">www.fernvaleshutters.com</p>
  </section>
</main>
</body>
</html>
```